Flyer for our prophetic church event

I need a flyer designed for the launching of our "Nine Radiant Lord's Day Gatherings" event. This event should high light the next 7 Sundays starting on February the 11th, 2018

Event Name:
Nine Radiant Lord's Days

Event Slogan or topic:
Go and tell John ... the blind see, the lame walk, the lepers are cleansed, the deaf hear, the dead are raised,
the poor have the gospel preached to them.

Speaker:
Prophet Tomas Okello

February 11th
February 18th
February 25th
March 4th
March 11th
March 18th
March 25th

Location:
Halvor Community Center
382 Wendle Street
Portland, ME 04102
United States

Time:
10:00AM - 12:00PM

We welcome you all in the name of Jesus Christ

Contact Info:
Tel:+1(207) 555 3184 - Email:contact@brightmeadowfold.org - Website: http://velkor.org

Target Market(s)

Young adults

Industry/Entity Type

Church

Font styles to use
Other font styles liked:
• Surprise me, I trust the designers skills

Colors

Designer to choose colors to be used in the design.

Requirements
Must have
• The Velkor logo
• Tomas Okello's picture
• The
Should not have
• The background of the Tomas Okello's picture

```html
<!DOCTYPE html>
<html lang="en">
<head>
<meta charset="utf-8">
<title>Nine Radiant Lord's Day Gatherings</title>
<link href="https://fonts.googleapis.com/css2?family=Michroma&family=Montserrat:wght@500;600;700&family=Open+Sans:wght@400;600;700&family=Signika:wght@500;600&display=swap" rel="stylesheet">
<style>
  :root{
    --sky-purple:#5a3f8f;
    --sky-pink:#e9a6c8;
    --sky-orange:#f2a35c;
    --white:#ffffff;
    --orange:#e8912c;
    --blue:#2f86d6;
    --blue-light:#4ea3e6;
    --grey-dark:#555a60;
    --grey-mid:#8a8e94;
    --plum:#a75c92;
    --ink:#3a3d42;
  }
  html,body{margin:0;padding:0;width:970px;height:1200px;overflow:hidden;background:#fff;}
  h1{margin:0;font-weight:400;}
  .flyer{position:relative;width:970px;height:1200px;overflow:hidden;
    background:linear-gradient(180deg,var(--sky-purple) 0%,#9a6fb8 12%,#f3d4e6 30%,#fff6f0 45%,#fff 62%,#fff 100%);
    font-family:"Open Sans",sans-serif;}
  .sky-art{position:absolute;left:0;top:0;width:970px;height:780px;
    background:
      radial-gradient(ellipse 260px 340px at 60px 330px,rgba(236,140,170,.55),transparent 70%),
      radial-gradient(ellipse 260px 340px at 910px 330px,rgba(236,140,170,.55),transparent 70%),
      radial-gradient(ellipse 300px 160px at 80px 640px,rgba(242,150,80,.55),transparent 70%),
      radial-gradient(ellipse 300px 160px at 900px 660px,rgba(242,150,80,.45),transparent 70%),
      radial-gradient(ellipse 320px 220px at 480px 230px,rgba(255,255,255,.85),transparent 70%);}
  .hero-numeral{position:absolute;left:236px;top:40px;font-family:"Michroma",sans-serif;font-size:290px;line-height:1;
    background:linear-gradient(180deg,#b46aa8 0%,#7c4f9e 100%);-webkit-background-clip:text;background-clip:text;color:transparent;}
  .hero-base{position:absolute;left:292px;top:340px;width:500px;height:3px;background:rgba(255,255,255,.8);}
  .speaker-portrait-top{position:absolute;left:520px;top:50px;width:200px;height:290px;border-radius:90px 90px 0 0;
    background:linear-gradient(180deg,#6b4a3c 0%,#2d2d36 55%,#1f2128 100%);}
  .title-main{position:absolute;left:0;width:970px;top:352px;text-align:center;font-family:"Michroma",sans-serif;font-size:88px;line-height:1;
    background:linear-gradient(180deg,#8cc6f2 0%,#2f7fd0 60%,#1f5fae 100%);-webkit-background-clip:text;background-clip:text;color:transparent;letter-spacing:1px;}
  .title-sub{position:absolute;left:0;width:970px;top:464px;text-align:center;font-family:"Montserrat",sans-serif;font-weight:600;font-size:32px;line-height:1;letter-spacing:5px;color:var(--grey-mid);}
  .date-line{position:absolute;left:0;width:970px;top:528px;height:50px;}
  .date-bar{position:absolute;top:22px;height:20px;background:rgba(255,255,255,.9);}
  .date-bar.left{left:0;width:250px}
  .date-bar.right{right:0;width:255px}
  .date-tag{position:absolute;left:310px;top:0;background:var(--blue);color:#fff;font-family:"Montserrat",sans-serif;font-weight:700;font-size:11px;line-height:14px;padding:1px 6px;}
  .date-text{position:absolute;left:0;width:970px;top:12px;text-align:center;font-family:"Montserrat",sans-serif;font-weight:700;font-size:32px;line-height:1.1;color:var(--orange);}
  .date-text sup{font-size:17px}
  .week{position:absolute;height:52px;width:230px;}
  .week .num{position:absolute;left:0;top:0;width:48px;height:52px;background:var(--grey-dark);color:#fff;font-family:"Montserrat",sans-serif;font-weight:600;font-size:32px;text-align:center;line-height:52px;}
  .week .day{position:absolute;left:60px;top:1px;font-size:15px;font-weight:600;color:var(--orange);}
  .week .rule{position:absolute;left:60px;top:24px;width:170px;height:1px;background:#c7c7c7;}
  .week .topic{position:absolute;left:60px;top:26px;font-size:18px;font-weight:600;color:var(--blue-light);white-space:nowrap;}
  .finale{position:absolute;z-index:2;left:200px;top:720px;width:570px;height:66px;}
  .finale .num{position:absolute;left:0;top:0;width:76px;height:66px;background:var(--grey-dark);color:#fff;font-family:"Montserrat",sans-serif;font-weight:600;font-size:44px;text-align:center;line-height:66px;}
  .finale .day{position:absolute;right:0;top:0;width:140px;height:30px;background:var(--orange);color:#fff;font-size:17px;font-weight:600;text-align:center;line-height:30px;}
  .finale .topic{position:absolute;left:76px;right:0;top:30px;height:36px;background:var(--blue);color:#fff;font-size:21px;font-weight:600;line-height:36px;padding-left:16px;white-space:nowrap;}
  .details-band{position:absolute;left:200px;top:832px;width:770px;height:145px;background:var(--plum);}
  .speaker-portrait{position:absolute;left:10px;top:740px;width:190px;height:237px;border-radius:95px 95px 0 0;
    background:linear-gradient(180deg,#5b3f34 0%,#2c2e36 45%,#20222a 100%);}
  .label{position:absolute;font-family:"Montserrat",sans-serif;font-weight:600;font-size:22px;line-height:1.2;color:#f4b267;}
  .value{position:absolute;font-family:"Montserrat",sans-serif;font-weight:600;font-size:24px;line-height:1.2;color:#fff;white-space:nowrap;}
  .address{position:absolute;left:256px;top:952px;font-size:15px;line-height:1.2;font-weight:600;color:#fff;white-space:nowrap;}
  .welcome{position:absolute;left:0;width:970px;top:992px;text-align:center;font-family:"Signika",sans-serif;font-weight:500;font-size:24px;line-height:1.2;color:var(--orange);}
  .blessing{position:absolute;left:0;width:970px;top:1022px;text-align:center;font-family:"Signika",sans-serif;font-weight:600;font-size:62px;line-height:1;color:var(--blue);}
  .contact-rule{position:absolute;left:0;top:1090px;width:970px;height:7px;background:var(--blue);}
  .contact-icon{position:absolute;top:1073px;width:46px;height:40px;background:#fff;}
  .contact{position:absolute;top:1134px;font-family:"Open Sans",sans-serif;font-weight:600;font-size:21px;line-height:1.2;color:var(--ink);white-space:nowrap;}
</style>
</head>
<body>
<main class="flyer">
  <div class="sky-art" role="img" aria-label="Soft sky with clouds and open hands in pink, orange and purple light"></div>

  <div class="hero-numeral">9</div>
  <div class="speaker-portrait-top" role="img" aria-label="Cut-out portrait of Prophet Tomas Okello"></div>
  <div class="hero-base"></div>

  <h1 class="title-main">RADIANT</h1>
  <div class="title-sub">LORD'S DAY GATHERINGS</div>

  <div class="date-line">
    <div class="date-bar left"></div>
    <div class="date-bar right"></div>
    <div class="date-tag">STARTING ON</div>
    <div class="date-text">February the 11<sup>th</sup>, 2018</div>
  </div>

  <div class="week" style="left:117px;top:585px"><div class="num">1</div><div class="day">February 11th</div><div class="rule"></div><div class="topic">Go and tell John</div></div>
  <div class="week" style="left:372px;top:585px"><div class="num">2</div><div class="day">February 18th</div><div class="rule"></div><div class="topic">The blind see</div></div>
  <div class="week" style="left:630px;top:585px"><div class="num">3</div><div class="day">February 25th</div><div class="rule"></div><div class="topic">The lame walk</div></div>
  <div class="week" style="left:117px;top:650px"><div class="num">4</div><div class="day">March 4th</div><div class="rule"></div><div class="topic">The lepers cleansed</div></div>
  <div class="week" style="left:372px;top:650px"><div class="num">5</div><div class="day">March 11th</div><div class="rule"></div><div class="topic">The deaf hear</div></div>
  <div class="week" style="left:630px;top:650px"><div class="num">6</div><div class="day">March 18th</div><div class="rule"></div><div class="topic">The dead raised</div></div>

  <div class="finale">
    <div class="num">7</div>
    <div class="day">March 25th</div>
    <div class="topic">The poor have the gospel preached to them.</div>
  </div>

  <div class="details-band"></div>
  <div class="speaker-portrait" role="img" aria-label="Portrait of Prophet Tomas Okello in a dark suit, background removed"></div>
  <div class="label" style="left:256px;top:846px">Speaker:</div>
  <div class="value" style="left:256px;top:876px">Prophet Tomas Okello</div>
  <div class="label" style="left:595px;top:846px">Time:</div>
  <div class="value" style="left:595px;top:876px">10:00AM - 12:00PM</div>
  <div class="label" style="left:256px;top:920px">Location:</div>
  <div class="address">Halvor Community Center , 382 Wendle Street , Portland, ME 04102 , US</div>

  <div class="welcome">We welcome you all in the name of</div>
  <div class="blessing">Jesus Christ</div>

  <div class="contact-rule"></div>
  <svg class="contact-icon" style="left:164px" viewBox="0 0 46 40" aria-label="Phone">
    <path d="M8 14c0-5 6-7 15-7s15 2 15 7v3h-8v-4H16v4H8z" fill="#4a4d52"/>
    <path d="M13 20h20l3 14H10z" fill="#4a4d52"/>
    <circle cx="23" cy="27" r="3.5" fill="#fff"/>
  </svg>
  <svg class="contact-icon" style="left:464px" viewBox="0 0 46 40" aria-label="Email">
    <rect x="7" y="9" width="32" height="22" fill="#4a4d52"/>
    <path d="M8 10l15 12 15-12" fill="none" stroke="#fff" stroke-width="2.5"/>
  </svg>
  <svg class="contact-icon" style="left:757px" viewBox="0 0 46 40" aria-label="Website">
    <circle cx="23" cy="20" r="14" fill="none" stroke="#4a4d52" stroke-width="3"/>
    <ellipse cx="23" cy="20" rx="6" ry="14" fill="none" stroke="#4a4d52" stroke-width="2.5"/>
    <path d="M9 20h28M12 13h22M12 27h22" stroke="#4a4d52" stroke-width="2.5"/>
  </svg>

  <div class="contact" style="left:100px">+1(207) 555 3184</div>
  <div class="contact" style="left:360px">contact@brightmeadowfold.org</div>
  <div class="contact" style="left:717px">http://velkor.org</div>
</main>
</body>
</html>
```